New Business Card Design Project

Make a kick ass business card for The Otter Tea Mug, using the designs. I also might like the 2nd place design logo on the back? Maybe all black with that? Not sure. Also, I'm cool with it being on metal, plastic, glass? or whatever for the business card. Maybe shaped like a shark? Let me know what else you need? Would like designs in the next day or so. Thank you.
Target Market(s)
Anyone that is cool
Contact Information for Business Card
Name: Dorian Fenwick
Phone: 317.594.8126
inventor/creator/entrepreneur/owner
www.theottertyeamug.example
social media links
https://www.facebook.com/theottertyeamug
https://twitter.com/otter_brew
https://www.instagram.com/theottertyeamug/
I'll get the Pinterest one soon
Colors
Designer to choose colors to be used in the design.
Requirements
Must have
- The Otter Tea Mug
- www.theottertyeamug.example
- social media tags?
- My logos and picture/photo of wine glass
Nice to have
- Maybe shaped like a wine glass or shark
- I'll let you decide but my same colors from my website would be nice

```html
<!DOCTYPE html>
<html lang="en">
<head>
<meta charset="utf-8">
<title>The Otter Tea Mug – Business Card</title>
<link rel="stylesheet" href="https://fonts.googleapis.com/css2?family=Lato:wght@400&family=Montserrat:wght@700&display=swap">
<style>
  :root {
    --backdrop: #4a4a4a;
    --card: #231f20;
    --red: #c1272d;
    --red-deep: #8e1b20;
    --ink-light: #e6e6e6;
  }
  * { margin: 0; padding: 0; box-sizing: border-box; }
  html, body { width: 1200px; height: 1056px; overflow: hidden; }
  body {
    background: var(--backdrop);
    font-family: "Lato", Arial, sans-serif;
    position: relative;
  }
  .card {
    position: absolute;
    left: 220px;
    width: 760px;
    height: 434px;
    background: var(--card);
    overflow: hidden;
    box-shadow: 0 6px 18px rgba(0,0,0,0.35);
  }
  .card-front { top: 60px; }
  .card-back { top: 562px; }
  .waves { position: absolute; left: 0; top: 0; width: 760px; height: 434px; }

  .holder-name {
    position: absolute;
    right: 56px;
    top: 36px;
    font-family: "Montserrat", Arial, sans-serif;
    font-weight: 700;
    font-size: 32px;
    line-height: 1;
    color: var(--red);
    letter-spacing: 0.5px;
  }
  .holder-title {
    position: absolute;
    right: 44px;
    top: 78px;
    font-size: 17px;
    line-height: 1;
    color: var(--ink-light);
  }
  .title-rule {
    position: absolute;
    left: 70px;
    top: 92px;
    width: 320px;
    height: 2px;
    background: linear-gradient(90deg, var(--red-deep), var(--red));
  }
  .contact-list {
    position: absolute;
    left: 90px;
    top: 128px;
    list-style: none;
  }
  .contact-list li {
    display: flex;
    align-items: center;
    gap: 12px;
    height: 30px;
    font-size: 18px;
    color: var(--ink-light);
  }
  .contact-list li.gap-before { margin-top: 14px; }
  .contact-icon { width: 22px; height: 22px; flex: none; }

  .glass-art {
    position: absolute;
    left: 598px;
    top: 104px;
    width: 96px;
    height: 150px;
    background: radial-gradient(ellipse at 50% 35%, #5a1a1d 0%, #3a1c1e 60%, var(--card) 100%);
    border-radius: 40px 40px 10px 10px;
  }

  .brand-name {
    position: absolute;
    left: 0;
    width: 760px;
    top: 170px;
    text-align: center;
    font-family: "Lato", Arial, sans-serif;
    font-weight: 400;
    font-size: 50px;
    color: var(--ink-light);
    letter-spacing: 1px;
  }
</style>
</head>
<body>

<section class="card card-front" aria-label="Business card front">
  <svg class="waves" viewBox="0 0 760 434" aria-hidden="true">
    <defs>
      <linearGradient id="swoosh-front" x1="0" x2="1">
        <stop offset="0" stop-color="#231f20" stop-opacity="0"/>
        <stop offset="0.6" stop-color="#6e161a"/>
        <stop offset="1" stop-color="#8e1b20"/>
      </linearGradient>
    </defs>
    <path d="M0,376 C200,372 380,350 520,306 C620,276 700,256 760,250 L760,434 L0,434 Z" fill="var(--red)"/>
    <path d="M0,404 C200,400 400,376 540,336 C640,306 710,284 760,276" fill="none" stroke="var(--card)" stroke-width="9"/>
    <path d="M0,382 C180,380 330,366 450,330 C380,356 240,376 0,394 Z" fill="url(#swoosh-front)"/>
    <path d="M470,320 C580,282 680,262 760,258 L760,272 C680,278 580,296 470,320 Z" fill="#8e1b20"/>
  </svg>

  <h1 class="holder-name">DORIAN FENWICK</h1>
  <p class="holder-title">Inventor/Creator/Entrepreneur/Owner</p>
  <div class="title-rule"></div>

  <ul class="contact-list">
    <li>
      <svg class="contact-icon" viewBox="0 0 24 24" aria-hidden="true">
        <circle cx="12" cy="12" r="11" fill="none" stroke="var(--red)" stroke-width="1.5"/>
        <path d="M8 7 l2 -0.5 l1.2 2.6 l-1.3 1 c0.6 1.4 1.6 2.4 3 3 l1 -1.3 l2.6 1.2 l-0.5 2 c-4.5 0.3 -8.3 -3.5 -8 -8 z" fill="var(--red)"/>
      </svg>
      317.594.8126
    </li>
    <li>
      <svg class="contact-icon" viewBox="0 0 24 24" aria-hidden="true">
        <circle cx="12" cy="12" r="11" fill="none" stroke="var(--red)" stroke-width="1.5"/>
        <circle cx="12" cy="12" r="6" fill="none" stroke="var(--red)" stroke-width="1.3"/>
        <ellipse cx="12" cy="12" rx="2.6" ry="6" fill="none" stroke="var(--red)" stroke-width="1.1"/>
        <line x1="6" y1="12" x2="18" y2="12" stroke="var(--red)" stroke-width="1.1"/>
      </svg>
      www.theottertyeamug.example
    </li>
    <li class="gap-before">
      <svg class="contact-icon" viewBox="0 0 24 24" aria-hidden="true"><circle cx="12" cy="12" r="11" fill="none" stroke="var(--red)" stroke-width="1.5"/></svg>
      theottertyeamug
    </li>
    <li>
      <svg class="contact-icon" viewBox="0 0 24 24" aria-hidden="true"><circle cx="12" cy="12" r="11" fill="none" stroke="var(--red)" stroke-width="1.5"/></svg>
      theottertyeamug
    </li>
    <li>
      <svg class="contact-icon" viewBox="0 0 24 24" aria-hidden="true"><circle cx="12" cy="12" r="11" fill="none" stroke="var(--red)" stroke-width="1.5"/></svg>
      otter_brew
    </li>
    <li>
      <svg class="contact-icon" viewBox="0 0 24 24" aria-hidden="true"><circle cx="12" cy="12" r="11" fill="none" stroke="var(--red)" stroke-width="1.5"/></svg>
      theottertyeamug
    </li>
  </ul>

  <div class="glass-art" role="img" aria-label="Red outline illustration of a stemmed glass with the brand mascot inside"></div>
</section>

<section class="card card-back" aria-label="Business card back">
  <svg class="waves" viewBox="0 0 760 434" aria-hidden="true">
    <defs>
      <linearGradient id="swoosh-back" x1="0" x2="1">
        <stop offset="0" stop-color="#231f20" stop-opacity="0"/>
        <stop offset="0.5" stop-color="#6e161a"/>
        <stop offset="1" stop-color="#8e1b20"/>
      </linearGradient>
    </defs>
    <path d="M0,350 C160,330 300,320 420,318 C560,316 680,270 760,228 L760,434 L0,434 Z" fill="var(--red)"/>
    <path d="M0,388 C180,360 330,346 470,340 C600,334 700,292 760,262" fill="none" stroke="var(--card)" stroke-width="9"/>
    <path d="M0,372 C120,352 250,336 420,326 C280,344 150,362 0,384 Z" fill="url(#swoosh-back)"/>
    <path d="M440,312 C580,300 690,256 760,222 L760,240 C690,270 580,306 440,312 Z" fill="url(#swoosh-back)"/>
  </svg>

  <p class="brand-name">The Otter Tea Mug</p>
</section>

</body>
</html>
```